Wellness IV Billboard for Naturopathic Physicians.

We need a billboard design done. We have some templates. The client would like three options to choose from. The IV bag is important this is a wellness IV billboard. The fruit needs color added. The client wants it to be obvious this is about getting a wellness IV. Same day appts available. Bright fruit is in the IV is important. You can find out more about the client at www.velorin.clinic.

Target Market(s)

Missoula Montana

Industry/Entity Type

Health And Wellness

Font styles to use
Serif
Other font styles liked:
• see attached document with approved fonts

Colors

Designer to choose colors to be used in the design.

Requirements
Must have
• IV, logo, Wellness IVs, Same Day Appointments-See the template. Must use the graphic brand guidelines with font. Font used in template is approved to use.
Nice to have
• Must have iv bag filled with fruit and vegetables.
Should not have
• Use the attached template.

```html
<!DOCTYPE html>
<html lang="en">
<head>
<meta charset="utf-8">
<title>Velorin – IV Therapy Billboard</title>
<link rel="stylesheet" href="https://fonts.googleapis.com/css2?family=Arvo:wght@400;700&family=Roboto:ital,wght@0,300;0,500;1,300;1,500&display=swap">
<style>
  :root {
    --brand-green: #4b6a22;
    --board-white: #ffffff;
    --board-edge: #9a9a9a;
    --page-bg: #ffffff;
    --bag-light: #eef0ea;
    --citrus-yellow: #f3c21e;
    --citrus-orange: #ef8a1c;
    --leaf-green: #8fb33c;
  }
  * { margin: 0; padding: 0; box-sizing: border-box; }
  html, body {
    width: 1200px;
    height: 1199px;
    overflow: hidden;
    background: var(--page-bg);
  }
  .billboard {
    position: absolute;
    left: 40px;
    top: 344px;
    width: 1120px;
    height: 511px;
    background: var(--board-white);
    border: 1.5px solid var(--board-edge);
    color: var(--brand-green);
  }
  .brand {
    position: absolute;
    left: 73px;
    top: 130px;
    width: 245px;
    text-align: center;
  }
  .brand-dot {
    width: 72px;
    height: 72px;
    border-radius: 50%;
    background: var(--brand-green);
    margin: 0 auto 62px;
  }
  .brand-name {
    font-family: "Arvo", serif;
    font-weight: 700;
    font-size: 50px;
    line-height: 1;
    letter-spacing: 1px;
  }
  .headline {
    position: absolute;
    left: 337px;
    top: 88px;
    font-family: "Arvo", serif;
    font-weight: 700;
    font-size: 72px;
    line-height: 1;
    letter-spacing: 3px;
  }
  .tagline {
    position: absolute;
    left: 344px;
    top: 164px;
    font-family: "Arvo", serif;
    font-size: 19px;
    letter-spacing: 0.56em;
    line-height: 1;
  }
  .appointments {
    position: absolute;
    left: 375px;
    top: 259px;
    font-family: "Arvo", serif;
    font-size: 29px;
    line-height: 1;
  }
  .phone {
    position: absolute;
    left: 375px;
    top: 300px;
    font-family: "Roboto", sans-serif;
    font-size: 33px;
    line-height: 1;
  }
  .phone-label { font-style: italic; font-weight: 300; }
  .phone-number { font-weight: 500; }
  .web {
    position: absolute;
    left: 158px;
    top: 440px;
    line-height: 1;
    white-space: nowrap;
  }
  .web-label {
    font-family: "Roboto", sans-serif;
    font-style: italic;
    font-weight: 500;
    font-size: 24px;
    margin-right: 10px;
  }
  .web-address {
    font-family: "Arvo", serif;
    font-size: 25px;
    letter-spacing: 0.32em;
  }
  .iv-bag {
    position: absolute;
    left: 885px;
    top: 14px;
    width: 230px;
    height: 486px;
  }
</style>
</head>
<body>
  <section class="billboard">
    <div class="brand">
      <div class="brand-dot"></div>
      <div class="brand-name">VELORIN</div>
    </div>

    <h1 class="headline">IV THERAPY</h1>
    <p class="tagline">WELLNESS FROM WITH IN</p>

    <p class="appointments">SAME DAY APPOINTMENTS</p>
    <p class="phone"><span class="phone-label">CALL:</span><span class="phone-number">406.555.0142</span></p>

    <p class="web"><span class="web-label">LEARN MORE AT:</span><span class="web-address">WWW.VELORIN.CLINIC</span></p>

    <svg class="iv-bag" viewBox="0 0 230 486" role="img" aria-label="Photo of an IV bag filled with sliced citrus fruit and vegetables, with drip line below">
      <defs>
        <linearGradient id="bagFill" x1="0" y1="0" x2="0" y2="1">
          <stop offset="0" stop-color="var(--bag-light)"/>
          <stop offset="0.35" stop-color="#dfe6c8"/>
          <stop offset="0.6" stop-color="var(--citrus-yellow)"/>
          <stop offset="0.85" stop-color="var(--citrus-orange)"/>
          <stop offset="1" stop-color="#f0d9a8"/>
        </linearGradient>
      </defs>
      <rect x="5" y="10" width="220" height="320" rx="22" fill="url(#bagFill)"/>
      <rect x="108" y="330" width="14" height="60" fill="#dcdcd4"/>
      <rect x="113" y="390" width="5" height="92" fill="#e4e4de"/>
    </svg>
  </section>
</body>
</html>
```